Disposable Mini Sauce Pot Design for Asian Chain Food Brands

We operate a Hainan Chicken Rice takeout brand under the name Wokly8, with our official website: www.Wokly8.com.
We offer four signature house sauces and are launching brand-new packaging for our sauce line. We require custom graphic designs exclusively for the sauce cup lids.
Product Material & Base Specs
The sauce cups are made of PP plastic, available in two translucent base options: Translucent White and Translucent Orange.
Four Sauce Varieties for Individual Lid Designs
1. Red Sauce – Fried Sweet Chili Sauce
2.Green Sauce – Scallion Oil Dressing
3.Sweet Soy Sauce
4.Sweet Red Sauce (Special for Fried Chicken)
Differentiate each sauce lid design through unique graphics, typography, or illustrative elements for easy customer identification.
The marking NET WT 2 OZ must be clearly printed on every lid.
**There is no need to print full descriptive text or the full name of the sauces on each lid; the design only needs to clearly differentiate the four sauce varieties.
**Please reference the original design style and brand color palette shown on our official website, and feel free to fully unleash your creativity.
Look and feel
Each slider illustrates characteristics of the customer's brand and the style your logo design should communicate.

```html
<!DOCTYPE html>
<html lang="en">
<head>
<meta charset="utf-8">
<title>Wokly8 Sauce Lids</title>
<link rel="stylesheet" href="https://fonts.googleapis.com/css2?family=Oswald:wght@400;600&display=swap">
<style>
  :root {
    --lid-orange: #ff4a06;
    --chili: #ffa300;
    --scallion: #aeff00;
    --soy: #4e1412;
    --red-sauce: #990000;
    --ink: #ffffff;
    --page: #ffffff;
  }
  * { margin: 0; padding: 0; box-sizing: border-box; }
  html, body { width: 1200px; height: 1000px; overflow: hidden; background: var(--page); }
  body { position: relative; font-family: "Oswald", sans-serif; color: var(--ink); }

  .lid {
    position: absolute;
    width: 324px; height: 287px;
    background: var(--lid-orange);
    border-radius: 46px;
    box-shadow: 0 2px 5px rgba(0,0,0,0.18);
    overflow: hidden;
  }
  .lid--chili { left: 243px; top: 180px; }
  .lid--scallion { left: 633px; top: 180px; }
  .lid--soy { left: 243px; top: 533px; }
  .lid--red { left: 633px; top: 533px; }

  .bubble { position: absolute; left: 0; top: 0; width: 324px; height: 287px; }
  .lid--chili .bubble-shape { fill: var(--chili); }
  .lid--scallion .bubble-shape { fill: var(--scallion); }
  .lid--soy .bubble-shape { fill: var(--soy); }
  .lid--red .bubble-shape { fill: var(--red-sauce); }

  .sauce-name {
    position: absolute;
    left: 24px; top: 10px; width: 276px; height: 184px;
    display: flex; flex-direction: column; align-items: center; justify-content: center;
    text-align: center; text-transform: uppercase;
  }
  .sauce-name__main { font-weight: 600; font-size: 42px; line-height: 44px; letter-spacing: 0.2px; }
  .sauce-name__tag { font-weight: 400; font-size: 25px; line-height: 30px; }
  .sauce-name__tag--small { font-size: 22px; line-height: 25px; }

  .brand {
    position: absolute; left: 14px; top: 212px; width: 86px;
    text-align center;
    text-align: center; font-weight: 600; font-size: 26px; line-height: 1;
  }
  .net-weight {
    position: absolute; left: 108px; top: 236px;
    font-weight: 600; font-size: 24px; line-height: 1; letter-spacing: 0.2px;
    white-space: nowrap;
  }
  .mascot {
    position: absolute; left: 246px; top: 198px; width: 62px; height: 74px;
    background: var(--ink);
    border-radius: 45% 55% 50% 50% / 40% 45% 55% 60%;
  }
</style>
</head>
<body>

  <section class="lid lid--chili">
    <svg class="bubble" viewBox="0 0 568 503" aria-hidden="true">
      <path class="bubble-shape" d="M291,340 L403,355 L390,327 C480,305 525,255 525,185 C525,90 420,17 285,17 C150,17 43,90 43,185 C43,280 130,342 291,340 Z"/>
    </svg>
    <h2 class="sauce-name">
      <span class="sauce-name__main">Fried<br>Sweet Chili<br>Sauce</span>
    </h2>
    <p class="brand">Wokly8</p>
    <p class="net-weight">NET WT 2 OZ</p>
    <div class="mascot" role="img" aria-label="White chick mascot illustration"></div>
  </section>

  <section class="lid lid--scallion">
    <svg class="bubble" viewBox="0 0 568 503" aria-hidden="true">
      <path class="bubble-shape" d="M291,340 L403,355 L390,327 C480,305 525,255 525,185 C525,90 420,17 285,17 C150,17 43,90 43,185 C43,280 130,342 291,340 Z"/>
    </svg>
    <h2 class="sauce-name">
      <span class="sauce-name__tag">Green Sauce</span>
      <span class="sauce-name__main">Scallion Oil<br>Dressing</span>
    </h2>
    <p class="brand">Wokly8</p>
    <p class="net-weight">NET WT 2 OZ</p>
    <div class="mascot" role="img" aria-label="White chick mascot illustration"></div>
  </section>

  <section class="lid lid--soy">
    <svg class="bubble" viewBox="0 0 568 503" aria-hidden="true">
      <path class="bubble-shape" d="M291,340 L403,355 L390,327 C480,305 525,255 525,185 C525,90 420,17 285,17 C150,17 43,90 43,185 C43,280 130,342 291,340 Z"/>
    </svg>
    <h2 class="sauce-name">
      <span class="sauce-name__main">Sweet Soy<br>Sauce</span>
    </h2>
    <p class="brand">Wokly8</p>
    <p class="net-weight">NET WT 2 OZ</p>
    <div class="mascot" role="img" aria-label="White chick mascot illustration"></div>
  </section>

  <section class="lid lid--red">
    <svg class="bubble" viewBox="0 0 568 503" aria-hidden="true">
      <path class="bubble-shape" d="M291,340 L403,355 L390,327 C480,305 525,255 525,185 C525,90 420,17 285,17 C150,17 43,90 43,185 C43,280 130,342 291,340 Z"/>
    </svg>
    <h2 class="sauce-name">
      <span class="sauce-name__tag sauce-name__tag--small">Special for<br>Fried Chicken</span>
      <span class="sauce-name__main">Sweet Red<br>Sauce</span>
    </h2>
    <p class="brand">Wokly8</p>
    <p class="net-weight">NET WT 2 OZ</p>
    <div class="mascot" role="img" aria-label="White chick mascot illustration"></div>
  </section>

</body>
</html>
```